Marta Gellworth Name Card Design

Hello Designers,
I wanna have a name card with these details below:
Name: Marta Gellworth
Job Title: Doctor
Address: 2318 Birch Lane, Tacoma, WA, US
Phone: 9517380294
Slogan on card: Health care 24/7, Whenever you need, we're there!
I love yellows colors, red and white. It would be nice if my card would be designed with these colors.

Doctor

```html
<!DOCTYPE html>
<html lang="en">
<head>
<meta charset="utf-8">
<title>Marta Gellworth Name Card</title>
<link rel="stylesheet" href="https://fonts.googleapis.com/css2?family=Lato:ital,wght@0,400;0,700;1,400&display=swap">
<style>
  :root {
    --card-red: #7a0000;
    --accent-orange: #ff8f00;
    --accent-yellow: #ffc531;
    --text-white: #ffffff;
    --text-soft: #f3dede;
  }
  html, body {
    margin: 0;
    padding: 0;
    width: 1200px;
    height: 686px;
    overflow: hidden;
  }
  .name-card {
    position: relative;
    width: 1200px;
    height: 686px;
    background: var(--card-red);
    font-family: "Lato", sans-serif;
    color: var(--text-white);
  }
  .slogan {
    position: absolute;
    left: 0;
    right: 0;
    top: 92px;
    margin: 0;
    text-align: center;
    font-size: 30px;
    line-height: 1.3;
    font-weight: 400;
    color: var(--accent-yellow);
  }
  .slogan-tagline {
    display: block;
    font-size: 24px;
    color: var(--text-soft);
  }
  .holder-name {
    position: absolute;
    left: 0;
    right: 0;
    top: 296px;
    margin: 0;
    text-align: center;
    font-weight: 400;
    font-size: 85px;
    line-height: 1;
    letter-spacing: 0.5px;
  }
  .job-title {
    position: absolute;
    left: 0;
    right: 0;
    top: 405px;
    margin: 0;
    text-align: center;
    font-size: 34px;
    font-weight: 700;
    letter-spacing: 6px;
    text-transform: uppercase;
    color: var(--accent-orange);
  }
  .contact-row {
    position: absolute;
    left: 0;
    right: 0;
    top: 560px;
    display: flex;
    justify-content: center;
    gap: 70px;
    margin: 0;
    padding: 0;
    list-style: none;
    font-size: 25px;
    line-height: 32px;
  }
  .contact-item {
    display: flex;
    align-items: center;
    gap: 12px;
  }
  .contact-icon {
    width: 26px;
    height: 26px;
    fill: var(--accent-yellow);
    flex: none;
  }
  .base-band {
    position: absolute;
    left: 0;
    right: 0;
    bottom: 0;
    height: 42px;
    background: var(--accent-orange);
  }
</style>
</head>
<body>
  <main class="name-card">
    <p class="slogan">Health care 24/7
      <span class="slogan-tagline">Whenever you need, we're there!</span>
    </p>
    <h1 class="holder-name">Marta Gellworth</h1>
    <p class="job-title">Doctor</p>
    <ul class="contact-row">
      <li class="contact-item">
        <svg class="contact-icon" viewBox="0 0 24 24" aria-hidden="true">
          <path d="M12 2a7 7 0 0 0-7 7c0 5.2 7 13 7 13s7-7.8 7-13a7 7 0 0 0-7-7zm0 9.5A2.5 2.5 0 1 1 12 6.5a2.5 2.5 0 0 1 0 5z"/>
        </svg>
        <span>2318 Birch Lane, Tacoma, WA, US</span>
      </li>
      <li class="contact-item">
        <svg class="contact-icon" viewBox="0 0 24 24" aria-hidden="true">
          <path d="M6.6 10.8a15.1 15.1 0 0 0 6.6 6.6l2.2-2.2a1 1 0 0 1 1-.25 11.4 11.4 0 0 0 3.6.57 1 1 0 0 1 1 1V20a1 1 0 0 1-1 1A17 17 0 0 1 3 4a1 1 0 0 1 1-1h3.5a1 1 0 0 1 1 1c0 1.25.2 2.45.57 3.57a1 1 0 0 1-.25 1z"/>
        </svg>
        <span>9517380294</span>
      </li>
    </ul>
    <div class="base-band"></div>
  </main>
</body>
</html>
```